Build a Web page - Dovin Pratchell Homes, LLC - a custom home builder

We are a custom home builder in Wisconsin. Need a basic web page with a home page, About Us, Contact info, Gallery, and Testimonials page. Gallery will probably have sub-pages and each will have about ten pictures or less. I already own the domain and have web hosting through Wix, I just need the site built. Once the page is built I should be able to do the upkeep on it myself. If I need to add pictures or whatever.
Updates

Project Deadline Extended
Reason: I am still looking through designs and will select soon - thank you!

Target Market(s)

Gen X and Millennials who are looking to build a home. Custom built homes - not generic spec homes.

Industry/Entity Type

Home Builder

Number of Pages Required

5+ page

Font styles to use
Sans Serif

Colors
ffffff
ec1f27
000000
9d9d9d

Requirements
Must have
• I have no idea if I want coded or in coded. I'm not sure of the difference and why I would want one over the other.
Nice to have
• We like the following colors - red, black, gray, white.
Should not have
• not a big fan of clip art like hammers, tape measures, etc. Must look professional.

```html
<!DOCTYPE html>
<html lang="en">
<head>
<meta charset="utf-8">
<title>Dovin Pratchell Homes, LLC</title>
<link href="https://fonts.googleapis.com/css2?family=Lato:wght@300;400;700;900&display=swap" rel="stylesheet">
<style>
:root{
  --red:#c8202a;
  --red-bright:#ec1f27;
  --ink:#222222;
  --text:#555555;
  --muted:#9d9d9d;
  --white:#ffffff;
  --panel:#f1f1f1;
  --footer:#262626;
  --footer-dark:#151515;
  --line:#dddddd;
}
*{margin:0;padding:0;box-sizing:border-box}
html,body{width:673px;height:1200px;overflow:hidden;background:var(--white)}
body{font-family:"Lato",Arial,sans-serif;color:var(--text);position:relative}

/* header */
.site-header{position:absolute;left:0;top:0;width:673px;height:36px;background:var(--white);z-index:3;box-shadow:0 1px 3px rgba(0,0,0,.1)}
.main-nav{position:absolute;left:307px;top:0;display:flex;height:36px}
.main-nav a{display:block;padding:0 10px;line-height:36px;font-size:9px;color:var(--ink);text-decoration:none}
.main-nav a.active{background:var(--red);color:var(--white)}
.brand{position:absolute;left:94px;top:6px;width:90px;height:80px;background:var(--white);border:2px solid #e3e3e3;z-index:4;display:flex;flex-direction:column;align-items:center;justify-content:center;gap:4px}
.brand-mark{width:14px;height:14px;background:var(--red)}
.brand-name{font-size:9px;font-weight:700;color:#444;text-align:center;line-height:1.25;letter-spacing:.5px}

/* hero */
.hero{position:absolute;left:0;top:36px;width:673px;height:341px}
.hero-photo{position:absolute;inset:0;background:linear-gradient(180deg,#e9ecef 0%,#d9d6d1 35%,#b9a393 60%,#93a06b 82%,#7c8f57 100%)}
.hero-veil{position:absolute;inset:0;background:rgba(255,255,255,.45)}
.hero-title{position:absolute;left:0;width:673px;top:112px;text-align:center;font-size:27px;font-weight:400;color:#3a3a3a;letter-spacing:.3px}
.hero-title span{color:var(--red);font-weight:400}
.hero-sub{position:absolute;left:190px;width:293px;top:148px;text-align:center;font-size:13px;line-height:1.3;color:#3a3a3a}
.btn-red{position:absolute;background:var(--red);color:var(--white);font-size:10px;text-align:center;letter-spacing:.3px}
.hero .btn-red{left:291px;top:215px;width:90px;height:27px;line-height:27px}
.hero-arrow{position:absolute;top:152px;width:12px;height:22px}

/* sections */
.section-title{position:absolute;left:0;width:673px;text-align:center;font-size:18px;font-weight:400;color:var(--ink)}
.section-title span{color:var(--red)}
.rule{position:absolute;left:316px;width:40px;height:1px;background:var(--line)}
.lead{position:absolute;left:200px;width:273px;text-align:center;font-size:8.5px;line-height:1.5;color:var(--text)}

.project-grid{position:absolute;left:94px;top:496px;width:485px;display:grid;grid-template-columns:repeat(4,1fr);gap:12px}
.project{height:110px;border:3px solid var(--white);box-shadow:0 1px 4px rgba(0,0,0,.25)}
.p1{background:linear-gradient(160deg,#7a4a2c,#c49a72 60%,#e7dccd)}
.p2{background:linear-gradient(180deg,#9fb8d6 0%,#cfc7bb 45%,#6f8d4a 100%)}
.p3{background:linear-gradient(170deg,#e6e1d8,#b39f86 60%,#6b5642)}
.p4{background:linear-gradient(165deg,#d7c3a6,#8a6a4c 60%,#3e2e22)}

.testimonial-head{position:absolute;left:270px;top:694px;display:flex;gap:8px;align-items:center}
.avatar{width:34px;height:34px;border-radius:50%;background:linear-gradient(160deg,#c99d84,#6b4a3a)}
.t-name{font-size:11px;color:var(--ink)}
.t-name small{font-size:7px;color:var(--muted);margin-left:4px}
.stars{display:flex;gap:1px;align-items:center;margin-top:3px;font-size:7px;color:var(--muted)}
.quote{position:absolute;left:0;width:673px;top:747px;text-align:center;font-size:8px;font-weight:700;color:#444}
.t-body{position:absolute;left:150px;width:373px;top:766px;text-align:center;font-size:8px;line-height:1.55;color:var(--text)}
.pager{position:absolute;top:822px;left:316px;display:flex;gap:4px}
.pager span{width:17px;height:16px;border:1px solid #777;display:flex;align-items:center;justify-content:center}

/* contact band */
.contact-band{position:absolute;left:0;top:886px;width:673px;height:240px;background:var(--panel)}
.col-title{position:absolute;top:40px;font-size:16px;font-weight:400;color:#444}
.col-title span{color:var(--red)}
.field{position:absolute;left:96px;width:138px;height:20px;background:var(--white);border:1px solid var(--line);font-size:7px;color:#aaa;padding:6px 6px}
.contact-band .btn-red{left:176px;top:180px;width:58px;height:18px;line-height:18px;font-size:7px}
.map{position:absolute;left:271px;top:74px;width:151px;height:126px;background:linear-gradient(135deg,#e4e9ee,#c9d6e2 55%,#dfe5ea);border:1px solid var(--line)}
.info{position:absolute;left:455px;font-size:9px;color:#444;line-height:1.45}
.info-line{display:flex;align-items:center;gap:5px}
.info-line svg{width:8px;height:8px}
.socials{position:absolute;left:455px;top:174px;display:flex;gap:4px}
.socials span{width:14px;height:14px;border-radius:50%;border:1px solid #4a6fa5}

/* footer */
.site-footer{position:absolute;left:0;top:1126px;width:673px;height:47px;background:var(--footer);display:flex;justify-content:center;align-items:center;gap:48px}
.site-footer a{font-size:8px;color:#aaa;text-decoration:none;letter-spacing:.5px}
.copyright{position:absolute;left:0;top:1173px;width:673px;height:27px;background:var(--footer-dark);color:#bbb;font-size:9px;text-align:center;line-height:27px}
</style>
</head>
<body>

<header class="site-header">
  <nav class="main-nav">
    <a class="active" href="#">Home</a>
    <a href="#">About Us</a>
    <a href="#">Gallery</a>
    <a href="#">Testimonials</a>
    <a href="#">Contact Us</a>
  </nav>
</header>
<div class="brand">
  <div class="brand-mark"></div>
  <div class="brand-name">DOVIN<br>PRATCHELL<br>HOMES</div>
</div>

<section class="hero">
  <div class="hero-photo" role="img" aria-label="Photo of a custom-built home with a tan exterior, lawn and young tree"></div>
  <div class="hero-veil"></div>
  <h1 class="hero-title">WELCOME TO <span>DOVIN PRATCHELL</span></h1>
  <p class="hero-sub">Lorem Ipsum is simply dummy text of the printing and typesetting industry.</p>
  <div class="btn-red">CONTACT US</div>
  <svg class="hero-arrow" style="left:6px" viewBox="0 0 12 22"><path d="M10 2 L2 11 L10 20" fill="none" stroke="#fff" stroke-width="2.5"/></svg>
  <svg class="hero-arrow" style="right:6px" viewBox="0 0 12 22"><path d="M2 2 L10 11 L2 20" fill="none" stroke="#fff" stroke-width="2.5"/></svg>
</section>

<h2 class="section-title" style="top:406px"><span>Recent</span> Projects</h2>
<div class="rule" style="top:434px"></div>
<p class="lead" style="top:442px">It is a long established fact that a reader will be distracted by the readable content of a page when looking at its layout.</p>

<div class="project-grid">
  <div class="project p1" role="img" aria-label="Interior staircase with wooden railing"></div>
  <div class="project p2" role="img" aria-label="Exterior of a new home with front lawn"></div>
  <div class="project p3" role="img" aria-label="Bright living room interior"></div>
  <div class="project p4" role="img" aria-label="Family room with fireplace"></div>
</div>

<h2 class="section-title" style="top:657px"><span>Client</span> Testimonials</h2>
<div class="rule" style="top:684px"></div>

<div class="testimonial-head">
  <div class="avatar" role="img" aria-label="Client portrait"></div>
  <div>
    <div class="t-name">Jordan <small>20th Sep, 2017</small></div>
    <div class="stars">
      <svg width="48" height="9" viewBox="0 0 50 9">
        <g fill="#f2b01e">
          <polygon points="4.5,0 5.7,3.2 9,3.3 6.4,5.4 7.3,8.7 4.5,6.8 1.7,8.7 2.6,5.4 0,3.3 3.3,3.2"/>
          <polygon transform="translate(10 0)" points="4.5,0 5.7,3.2 9,3.3 6.4,5.4 7.3,8.7 4.5,6.8 1.7,8.7 2.6,5.4 0,3.3 3.3,3.2"/>
          <polygon transform="translate(20 0)" points="4.5,0 5.7,3.2 9,3.3 6.4,5.4 7.3,8.7 4.5,6.8 1.7,8.7 2.6,5.4 0,3.3 3.3,3.2"/>
          <polygon transform="translate(30 0)" points="4.5,0 5.7,3.2 9,3.3 6.4,5.4 7.3,8.7 4.5,6.8 1.7,8.7 2.6,5.4 0,3.3 3.3,3.2"/>
          <polygon transform="translate(40 0)" points="4.5,0 5.7,3.2 9,3.3 6.4,5.4 7.3,8.7 4.5,6.8 1.7,8.7 2.6,5.4 0,3.3 3.3,3.2"/>
        </g>
      </svg>
      (5/5)
    </div>
  </div>
</div>
<p class="quote">Lorem Ipsum is simply dummy text of the printing and typesetting industry.</p>
<p class="t-body">It is a long established fact that a reader will be distracted by the readable content of a page when looking at its layout. The point of using Lorem Ipsum is that it has a more-or-less normal distribution of letters, as opposed to using 'Content here, content here', making it look like readable English.</p>
<div class="pager">
  <span><svg width="6" height="8" viewBox="0 0 6 8"><path d="M5 1 L1 4 L5 7" fill="none" stroke="#444" stroke-width="1.3"/></svg></span>
  <span><svg width="6" height="8" viewBox="0 0 6 8"><path d="M1 1 L5 4 L1 7" fill="none" stroke="#444" stroke-width="1.3"/></svg></span>
</div>

<section class="contact-band">
  <h3 class="col-title" style="left:96px"><span>Contact</span> Form</h3>
  <div class="field" style="top:74px">Name</div>
  <div class="field" style="top:100px">Email Address</div>
  <div class="field" style="top:126px;height:44px">Enter your message here</div>
  <div class="btn-red">SEND</div>

  <h3 class="col-title" style="left:271px"><span>Location</span> Map</h3>
  <div class="map" role="img" aria-label="Map showing the office location"></div>

  <h3 class="col-title" style="left:455px">Contact Info</h3>
  <div class="info" style="top:70px;color:#777">4821 Alder Crest Lane,<br>Madison, Wisconsin</div>
  <div class="info" style="top:112px">
    <div class="info-line"><svg viewBox="0 0 8 8"><path d="M1.5 0.5 L3 2.5 L2.2 3.4 Q3.2 5 4.6 5.8 L5.5 5 L7.5 6.5 L6.6 7.6 Q3.5 7.3 0.5 1.5 Z" fill="#444"/></svg>+1 (555) 014-2280</div>
    <div class="info-line"><svg viewBox="0 0 8 8"><path d="M1.5 0.5 L3 2.5 L2.2 3.4 Q3.2 5 4.6 5.8 L5.5 5 L7.5 6.5 L6.6 7.6 Q3.5 7.3 0.5 1.5 Z" fill="#444"/></svg>+1 (555) 014-3391</div>
    <div class="info-line"><svg viewBox="0 0 8 8"><rect x="0.5" y="1.5" width="7" height="5" fill="none" stroke="#444"/><path d="M0.5 1.5 L4 4.5 L7.5 1.5" fill="none" stroke="#444"/></svg>info@dovinpratchell.com</div>
  </div>
  <div class="socials"><span></span><span></span><span></span></div>
</section>

<footer class="site-footer">
  <a href="#">HOME</a>
  <a href="#">ABOUT US</a>
  <a href="#">GALLERY</a>
  <a href="#">TESTIMONIALS</a>
  <a href="#">CONTACT US</a>
</footer>
<div class="copyright">© 2017 Copyright DovinPratchell. All Rights Reserved</div>

</body>
</html>
```